New Interrior Decoration company needs new website

We need a website for our new company specialising in interior decoration to residential and commercial markets.
We supply and install decorative and printed films for office and home decoration such as feature walls.
We would like to keep the design simple and clean.

Target Market(s)

Architects and interior designaers

Industry/Entity Type

It Company

Number of Pages Required

5+ page

Font styles to use
Sans Serif

Requirements
Must have
• Home page,
• Services/products page (split into commercial and residential)
• Gallery (split into commercial and residential)
• contact form and page
Nice to have
• Very clean and minimalistic design.

```html
<!DOCTYPE html>
<html lang="en">
<head>
<meta charset="utf-8">
<title>Lumen Interiors – Home</title>
<link href="https://fonts.googleapis.com/css2?family=Open+Sans:wght@400;600;700&family=Raleway:wght@400;500;600&display=swap" rel="stylesheet">
<style>
:root{
  --blue:#0b5cb8;
  --blue-light:#2a78d6;
  --dark:#3a3a3a;
  --darker:#333333;
  --text:#333333;
  --muted:#666666;
  --soft-bg:#f2f2f2;
  --white:#ffffff;
}
*{margin:0;padding:0;box-sizing:border-box}
html,body{width:1200px;height:2278px;overflow:hidden}
body{font-family:"Open Sans",sans-serif;color:var(--text);background:var(--white);position:relative}
.abs{position:absolute}

/* Header */
.top-rule{left:0;top:0;width:1200px;height:6px;background:var(--blue)}
.brand{left:77px;top:32px;height:62px;display:flex;align-items:center;gap:14px;font-family:"Open Sans",sans-serif;font-weight:700;font-size:30px;color:var(--darker);line-height:1;white-space:nowrap}
.brand-square{width:58px;height:58px;background:var(--blue);flex:none}
.header-mail{left:623px;top:14px;display:flex;align-items:center;gap:8px;font-size:17px;color:var(--text)}
.header-phone{left:887px;top:0;width:236px;height:51px;background:var(--blue);border-radius:0 0 6px 6px;display:flex;align-items:center;justify-content:center;gap:10px;color:var(--white);font-weight:700;font-size:22px}
.main-nav{left:488px;top:65px;display:flex;height:47px;font-size:20px}
.main-nav a{color:var(--darker);text-decoration:none;display:flex;align-items:center;justify-content:center;height:47px}
.main-nav .active{background:var(--blue);color:var(--white);width:103px}

/* Hero */
.hero{left:0;top:149px;width:1200px;height:573px;background:linear-gradient(90deg,#e9ecef 0%,#d9dde1 40%,#b9c3cc 60%,#cfd6dc 100%)}

/* Services band */
.service{top:723px;height:229px;display:flex;padding-top:44px;color:var(--white)}
.service--residential{left:0;width:600px;background:var(--blue);padding-left:77px}
.service--commercial{left:600px;width:600px;background:var(--dark);padding-left:28px}
.service-thumb{width:207px;height:140px;border:2px solid var(--white);flex:none}
.service-body{margin-left:18px;width:258px}
.service-title{font-family:"Raleway",sans-serif;font-weight:500;font-size:26px;line-height:1;margin-top:2px;white-space:nowrap}
.service-text{font-size:15px;line-height:25px;margin-top:8px}
.read-link{display:flex;align-items:center;gap:6px;font-family:"Raleway",sans-serif;font-size:18px;margin-top:10px}

/* Welcome */
.welcome{left:0;top:952px;width:1200px;height:322px;text-align:center}
.welcome-title{font-family:"Raleway",sans-serif;font-weight:400;font-size:42px;color:var(--darker);margin-top:50px;letter-spacing:0.5px}
.welcome-title span,.gallery-title span{color:var(--blue)}
.welcome-text{width:860px;margin:24px auto 0;font-size:15.5px;line-height:25px;color:var(--muted)}
.btn{display:inline-flex;align-items:center;justify-content:center;background:var(--blue);color:var(--white);font-family:"Raleway",sans-serif;font-size:19px;border-radius:3px}
.welcome .btn{width:163px;height:51px;margin-top:20px}

/* Gallery */
.gallery{left:0;top:1274px;width:1200px;height:667px;background:var(--soft-bg)}
.gallery-title{position:absolute;left:0;width:1200px;top:48px;text-align:center;font-family:"Raleway",sans-serif;font-weight:400;font-size:42px;color:var(--darker)}
.gallery-tabs{position:absolute;left:402px;top:107px;display:flex;gap:22px}
.tab{width:187px;height:51px;display:flex;align-items:center;justify-content:center;font-family:"Raleway",sans-serif;font-size:25px;color:var(--white)}
.tab--residential{background:var(--blue)}
.tab--commercial{background:var(--dark)}
.gallery-grid{position:absolute;left:77px;top:183px;display:grid;grid-template-columns:repeat(4,234px);grid-auto-rows:155px;column-gap:37px;row-gap:22px}
.gallery-grid div{width:234px;height:155px}
.gallery .btn{position:absolute;left:526px;top:553px;width:148px;height:52px}

/* Footer */
.footer{left:0;top:1941px;width:1200px;height:286px;background:var(--blue);color:var(--white)}
.footer-col{position:absolute;top:0}
.footer-brand{left:77px;top:38px;display:flex;align-items:center;gap:8px;font-weight:700;font-size:20px;white-space:nowrap}
.footer-brand .brand-square{width:30px;height:30px;background:var(--white)}
.footer-about{left:77px;top:95px;width:225px;font-size:15px;line-height:25px}
.footer-heading{font-family:"Raleway",sans-serif;font-weight:400;font-size:24px;margin-top:27px}
.links{left:349px}
.links ul{list-style:none;margin-top:16px}
.links li{display:flex;align-items:center;gap:10px;font-size:18px;height:36.5px}
.contact{left:620px;width:240px}
.contact-row{display:flex;gap:10px;font-size:15px;line-height:22px;margin-top:12px}
.contact-row span{max-width:205px}
.contact-row.strong{font-weight:700}
.social{display:flex;gap:26px;margin-top:18px}
.social-btn{width:47px;height:47px;border:2px solid var(--white);border-radius:3px;display:flex;align-items:center;justify-content:center}
.social-btn--solid{background:var(--white)}
.newsletter{left:889px;width:234px}
.field{height:37px;background:var(--blue-light);color:var(--white);font-size:15px;display:flex;align-items:center;padding-left:9px;border-radius:3px;margin-top:16px}
.newsletter .field:first-of-type{margin-top:20px}
.subscribe{width:150px;height:46px;background:var(--white);color:var(--darker);font-family:"Raleway",sans-serif;font-size:20px;display:flex;align-items:center;justify-content:center;border-radius:3px;margin-top:16px}
.copyright{left:0;top:2227px;width:1200px;height:51px;background:var(--darker);color:var(--white);font-size:15px;display:flex;align-items:center;justify-content:center}
</style>
</head>
<body>

<div class="abs top-rule"></div>

<header>
  <div class="abs brand"><span class="brand-square"></span>LUMEN INTERIORS</div>
  <div class="abs header-mail">
    <svg width="20" height="15" viewBox="0 0 20 15"><rect x="1" y="1" width="18" height="13" rx="1.5" fill="none" stroke="#0b5cb8" stroke-width="2"/><path d="M1 2l9 7 9-7" fill="none" stroke="#0b5cb8" stroke-width="2"/></svg>
    info@lumeninteriors.com
  </div>
  <div class="abs header-phone">
    <svg width="22" height="22" viewBox="0 0 24 24"><path d="M6.6 10.8a15.1 15.1 0 006.6 6.6l2.2-2.2a1 1 0 011-.25 11.4 11.4 0 003.6.57 1 1 0 011 1V20a1 1 0 01-1 1A17 17 0 013 4a1 1 0 011-1h3.5a1 1 0 011 1c0 1.25.2 2.45.57 3.57a1 1 0 01-.25 1z" fill="#fff"/></svg>
    123 456 7890
  </div>
  <nav class="abs main-nav">
    <a class="active">HOME</a>
    <a style="width:127px">ABOUT</a>
    <a style="width:151px">SERVICES</a>
    <a style="width:141px">GALLERY</a>
    <a style="width:116px">CONTACT</a>
  </nav>
</header>

<div class="abs hero" role="img" aria-label="Bright office interior with a white textured feature wall, a yellow lounge chair and glass-walled meeting rooms"></div>

<section class="abs service service--residential">
  <div class="service-thumb" role="img" aria-label="Residential room with grey wall, pendant lamps and a sideboard" style="background:linear-gradient(135deg,#8c9298,#d8dadc)"></div>
  <div class="service-body">
    <h2 class="service-title">Residential Interiors</h2>
    <p class="service-text">Lorem Ipsum is simply dummy text of the printing and typesetting industry Lorem Ipsum...</p>
    <div class="read-link">READ MORE
      <svg width="12" height="12" viewBox="0 0 12 12"><path d="M1 1l5 5-5 5M6 1l5 5-5 5" fill="none" stroke="#fff" stroke-width="1.6"/></svg>
    </div>
  </div>
</section>

<section class="abs service service--commercial">
  <div class="service-thumb" role="img" aria-label="Commercial corridor with a printed feature wall of coloured circles" style="background:linear-gradient(135deg,#e7e4e0,#c9c3bd)"></div>
  <div class="service-body">
    <h2 class="service-title">Commercial Interiors</h2>
    <p class="service-text">Lorem Ipsum is simply dummy text of the printing and typesetting industry Lorem Ipsum...</p>
    <div class="read-link">READ MORE
      <svg width="12" height="12" viewBox="0 0 12 12"><path d="M1 1l5 5-5 5M6 1l5 5-5 5" fill="none" stroke="#fff" stroke-width="1.6"/></svg>
    </div>
  </div>
</section>

<section class="abs welcome">
  <h1 class="welcome-title">WELCOME TO <span>LUMEN INTERIORS</span></h1>
  <p class="welcome-text">Lorem Ipsum is simply dummy text of the printing and typesetting industry. Lorem Ipsum has been the industry's standard dummy text ever since the 1500s, when an unknown printer took a galley of type and scrambled it to make a type specimen book.</p>
  <span class="btn">READ MORE</span>
</section>

<section class="abs gallery">
  <h2 class="gallery-title">LATEST <span>GALLERY</span></h2>
  <div class="gallery-tabs">
    <span class="tab tab--residential">Residential</span>
    <span class="tab tab--commercial">Commercial</span>
  </div>
  <div class="gallery-grid">
    <div role="img" aria-label="Living room with striped wood-tone feature wall and red sofa" style="background:linear-gradient(135deg,#c9b27a,#b4453a)"></div>
    <div role="img" aria-label="White lounge chair against a dark rust wall with bookshelf" style="background:linear-gradient(135deg,#5a2a1c,#2a1a16)"></div>
    <div role="img" aria-label="Playroom with colourful printed wall" style="background:linear-gradient(135deg,#d66a72,#5b8fc9)"></div>
    <div role="img" aria-label="Grey wall with pendant lamps and a white sideboard" style="background:linear-gradient(135deg,#7f868c,#d4d6d8)"></div>
    <div role="img" aria-label="Open kitchen and dining area with white pendant lights" style="background:linear-gradient(135deg,#6b6660,#c9c4bc)"></div>
    <div role="img" aria-label="Olive textured wall with a low cabinet and framed print" style="background:linear-gradient(135deg,#8a8a5a,#c5c39a)"></div>
    <div role="img" aria-label="Lounge with mauve wall and white sectional sofa" style="background:linear-gradient(135deg,#7a4a55,#c9b8b4)"></div>
    <div role="img" aria-label="Living room with striped wood-tone feature wall and red sofa" style="background:linear-gradient(135deg,#c9b27a,#b4453a)"></div>
  </div>
  <span class="btn">VIEW ALL</span>
</section>

<footer class="abs footer">
  <div class="footer-col footer-brand"><span class="brand-square"></span>LUMEN INTERIORS</div>
  <p class="footer-col footer-about">Lorem Ipsum is simply dummy text of the printing and typesetting industry. Lorem Ipsum has been the industry's standard dummy text ever since the 1500.</p>

  <div class="footer-col links">
    <h3 class="footer-heading">Useful Links</h3>
    <ul>
      <li><svg width="16" height="10" viewBox="0 0 16 10"><path d="M0 5h14M10 1l4 4-4 4" fill="none" stroke="#fff" stroke-width="1.8"/></svg>Home</li>
      <li><svg width="16" height="10" viewBox="0 0 16 10"><path d="M0 5h14M10 1l4 4-4 4" fill="none" stroke="#fff" stroke-width="1.8"/></svg>About</li>
      <li><svg width="16" height="10" viewBox="0 0 16 10"><path d="M0 5h14M10 1l4 4-4 4" fill="none" stroke="#fff" stroke-width="1.8"/></svg>Services</li>
      <li><svg width="16" height="10" viewBox="0 0 16 10"><path d="M0 5h14M10 1l4 4-4 4" fill="none" stroke="#fff" stroke-width="1.8"/></svg>Gallery</li>
      <li><svg width="16" height="10" viewBox="0 0 16 10"><path d="M0 5h14M10 1l4 4-4 4" fill="none" stroke="#fff" stroke-width="1.8"/></svg>Contact</li>
    </ul>
  </div>

  <div class="footer-col contact">
    <h3 class="footer-heading">Get In Touch</h3>
    <div class="contact-row">
      <svg width="14" height="20" viewBox="0 0 14 20" style="flex:none"><path d="M7 0a7 7 0 00-7 7c0 5 7 13 7 13s7-8 7-13a7 7 0 00-7-7zm0 9.5A2.5 2.5 0 117 4.5a2.5 2.5 0 010 5z" fill="#fff"/></svg>
      <span>Lorem Ipsum is dummy text of the printing.</span>
    </div>
    <div class="contact-row strong">
      <svg width="18" height="18" viewBox="0 0 24 24" style="flex:none"><path d="M6.6 10.8a15.1 15.1 0 006.6 6.6l2.2-2.2a1 1 0 011-.25 11.4 11.4 0 003.6.57 1 1 0 011 1V20a1 1 0 01-1 1A17 17 0 013 4a1 1 0 011-1h3.5a1 1 0 011 1c0 1.25.2 2.45.57 3.57a1 1 0 01-.25 1z" fill="#fff"/></svg>
      <span>123 456 7890</span>
    </div>
    <div class="contact-row">
      <svg width="18" height="14" viewBox="0 0 20 15" style="flex:none;margin-top:4px"><rect x="1" y="1" width="18" height="13" rx="1.5" fill="none" stroke="#fff" stroke-width="2"/><path d="M1 2l9 7 9-7" fill="none" stroke="#fff" stroke-width="2"/></svg>
      <span>info@lumeninteriors.com</span>
    </div>
    <div class="social" aria-label="Social media links">
      <span class="social-btn social-btn--solid">
        <svg width="20" height="20" viewBox="0 0 20 20"><circle cx="15" cy="4" r="2.6" fill="#333"/><circle cx="5" cy="10" r="2.6" fill="#333"/><circle cx="15" cy="16" r="2.6" fill="#333"/><path d="M15 4L5 10l10 6" fill="none" stroke="#333" stroke-width="1.6"/></svg>
      </span>
      <span class="social-btn">
        <svg width="20" height="20" viewBox="0 0 20 20"><circle cx="15" cy="4" r="2.6" fill="#fff"/><circle cx="5" cy="10" r="2.6" fill="#fff"/><circle cx="15" cy="16" r="2.6" fill="#fff"/><path d="M15 4L5 10l10 6" fill="none" stroke="#fff" stroke-width="1.6"/></svg>
      </span>
      <span class="social-btn">
        <svg width="20" height="20" viewBox="0 0 20 20"><circle cx="15" cy="4" r="2.6" fill="#fff"/><circle cx="5" cy="10" r="2.6" fill="#fff"/><circle cx="15" cy="16" r="2.6" fill="#fff"/><path d="M15 4L5 10l10 6" fill="none" stroke="#fff" stroke-width="1.6"/></svg>
      </span>
    </div>
  </div>

  <div class="footer-col newsletter">
    <h3 class="footer-heading">Newsletter</h3>
    <div class="field">Enter Name</div>
    <div class="field">Enter Email</div>
    <div class="subscribe">SUBSCRIBE</div>
  </div>
</footer>

<div class="abs copyright">©&nbsp;<strong>LUMEN INTERIORS</strong>&nbsp;- 2016. All Rights Reserved.</div>

</body>
</html>
```